Business Card Design

I am an child sleep consultant. I would like the picture to be the background of the card and for my logo to be in the upper right hand corner. Other than that, the design is yours!!

Industry/Entity Type

Business

Contact Information for Business Card

Marla Okonov
Tidewell Nestling
Certified Child Sleep Consultant
(406) 555-0193
tidewellnestling.example

```html
<!DOCTYPE html>
<html lang="en">
<head>
<meta charset="UTF-8">
<title>Tidewell Nestling – Business Card</title>
<link rel="stylesheet" href="https://fonts.googleapis.com/css2?family=Didact+Gothic&display=swap">
<style>
  :root {
    --page: #ffffff;
    --frame: #7fd0f3;
    --accent-red: #e8202a;
    --panel-light: #e8eff8;
    --panel-mid: #0aa0dc;
    --panel-deep: #1c3f9c;
    --photo-light: #d9d9d6;
    --photo-mid: #a3a3a0;
    --photo-dark: #5d5e5b;
    --text-white: #ffffff;
    --text-yellow: #f4ef1a;
    --text-navy: #2b3794;
    --logo-ink: #2b3794;
  }
  * { margin: 0; padding: 0; box-sizing: border-box; }
  html, body {
    width: 1200px;
    height: 700px;
    overflow: hidden;
    background: var(--page);
    font-family: "Didact Gothic", "Helvetica Neue", Arial, sans-serif;
  }
  .card {
    position: relative;
    width: 1200px;
    height: 700px;
  }
  .card-frame {
    position: absolute;
    left: 26px;
    top: 26px;
    width: 1150px;
    height: 649px;
    border: 3px solid var(--frame);
  }
  .hero-photo {
    position: absolute;
    left: 29px;
    top: 29px;
    width: 1144px;
    height: 378px;
    background:
      radial-gradient(ellipse 230px 260px at 420px 210px, var(--photo-light) 0%, rgba(217,217,214,0) 100%),
      linear-gradient(90deg, var(--photo-mid) 0%, var(--photo-dark) 45%, var(--photo-mid) 75%, var(--photo-light) 100%);
  }
  .accent-band {
    position: absolute;
    left: 24px;
    top: 407px;
    width: 1154px;
    height: 12px;
    background: var(--accent-red);
  }
  .info-panel {
    position: absolute;
    left: 29px;
    top: 419px;
    width: 1144px;
    height: 253px;
    background: linear-gradient(90deg, var(--panel-light) 0%, #7fc0e8 22%, var(--panel-mid) 48%, #0873be 75%, var(--panel-deep) 100%);
  }
  .logo-box {
    position: absolute;
    left: 845px;
    top: 42px;
    width: 315px;
    height: 234px;
    background: #ffffff;
    display: flex;
    align-items: center;
    justify-content: center;
    gap: 12px;
  }
  .logo-mark {
    width: 22px;
    height: 22px;
    border-radius: 50%;
    background: var(--logo-ink);
  }
  .logo-name {
    font-size: 30px;
    color: var(--logo-ink);
  }
  .brand-name {
    position: absolute;
    right: 58px;
    top: 308px;
    font-size: 48px;
    color: var(--text-white);
    letter-spacing: 0.5px;
  }
  .person-name {
    position: absolute;
    left: 0;
    width: 1166px;
    top: 440px;
    text-align: center;
    font-size: 46px;
    color: var(--text-white);
  }
  .person-title {
    position: absolute;
    left: 0;
    width: 1166px;
    top: 498px;
    text-align: center;
    font-size: 28px;
    color: var(--text-yellow);
  }
  .contact {
    position: absolute;
    top: 585px;
    font-size: 28px;
  }
  .contact-mobile {
    left: 121px;
    color: var(--text-navy);
  }
  .contact-web {
    left: 642px;
    color: var(--text-white);
  }
</style>
</head>
<body>
  <div class="card">
    <div class="hero-photo" role="img" aria-label="Black and white portrait photograph of a smiling baby, used as the card background"></div>
    <div class="accent-band"></div>
    <div class="info-panel"></div>
    <div class="card-frame"></div>

    <div class="logo-box">
      <span class="logo-mark"></span>
      <span class="logo-name">Tidewell Nestling</span>
    </div>

    <p class="brand-name">Tidewell Nestling</p>

    <h1 class="person-name">Marla Okonov</h1>
    <p class="person-title">Certified Child Sleep Consultant</p>

    <p class="contact contact-mobile">Mobile : (406) 555-0193</p>
    <p class="contact contact-web">Website : www.tidewellnestling.example</p>
  </div>
</body>
</html>
```